Million Dollar Vehicle Design For Home Service Company

New design for Brightway Tradesmen (home service company) vehicles.

Both sides and back

We are a new (opening in about 30 days) home service company.

We will begin by offering residential electrical services and soon expand to a full line by adding handyman, heating, cooling. plumbing and drain cleaning.

Looking for simple. Not cluttered.

Minimalist - Less is More mindset, but it must catch the eye.

Here is a link the website prototype being built for us. It has a bit more stuff on it now than it will in its final version, but this will help you get a feel for the colors.

http://www.lanternquay.com/PROOF/brightway-tradesmen-4/

You may also find inspiration at sunnymarsh.com

**Also, please note that some of the attached files will differ from my requests due to changes being made as we get closer to opening. For example, the tagline is different.

Target Market(s)

Home Owners 35 - 65 years old.

Industry/Entity Type

Electrician

Font styles to use
Serif

Requirements
Must have
• Simple. Easy to read. Easy to understand what the company does and how to contact.
• Big Website
• Big Phone Number
• Big Name
• Website: GoBrightwayFix.com
• Phone number: 515-555-0187
• ***Tagline: Brightway, All the Way or You'll Save $39
• ***Please note the tagline in this brief is different than is in the attached image.
Nice to have
• We will be adding services in the future. It would be nice to consider how these will be displayed on the vehicle. For example, it should be listed that we provide expert electrical services. I want to be able to list other services such as plumbing, heating and cooling as we add them by modifying only few things on each vehicle.
Should not have
• Cluttered. Should not be difficult to understand within 1 second.

```html
<!DOCTYPE html>
<html lang="en">
<head>
<meta charset="utf-8">
<title>Brightway Tradesmen – Vehicle Wrap</title>
<link rel="stylesheet" href="https://fonts.googleapis.com/css2?family=Archivo:wght@700;800&family=Archivo+Black&family=Oswald:wght@500&display=swap">
<style>
  :root {
    --brand-orange: #f2561d;
    --brand-red: #e8321e;
    --ink: #151515;
    --band-dark: #2b2b2b;
    --wrap-white: #ffffff;
    --canvas: #f4f4f4;
    --panel-edge: #d6d6d6;
    --money-green: #1f8a2a;
    --art-fill: #f7d9cc;
  }
  html, body {
    margin: 0;
    padding: 0;
    width: 1200px;
    height: 1200px;
    overflow: hidden;
    background: var(--canvas);
  }
  .wrap-sheet { display: block; width: 1200px; height: 1200px; }
  .tagline { font-family: "Oswald", "Arial Narrow", sans-serif; font-weight: 500; fill: var(--ink); }
  .tagline .price { fill: var(--money-green); }
  .brand-name { font-family: "Archivo Black", "Arial Black", sans-serif; fill: var(--brand-red); }
  .service-chip { fill: var(--brand-red); }
  .service-label { font-family: "Archivo", Arial, sans-serif; font-weight: 700; fill: var(--wrap-white); }
  .web-address { font-family: "Archivo", Verdana, sans-serif; font-weight: 700; }
  .phone { font-family: "Archivo", Arial, sans-serif; font-weight: 800; fill: var(--wrap-white); }
  .panel-outline { fill: none; stroke: var(--panel-edge); stroke-width: 2; }
  .mascot-area { fill: var(--art-fill); }
</style>
</head>
<body>
<svg class="wrap-sheet" viewBox="0 0 1200 1200" xmlns="http://www.w3.org/2000/svg">
  <defs>
    <clipPath id="side-clip"><rect x="16" y="40" width="1168" height="460" rx="26"/></clipPath>
    <clipPath id="rear-clip"><rect x="384" y="608" width="432" height="452" rx="28"/></clipPath>
  </defs>

  <!-- Side panel -->
  <g class="side-panel">
    <g clip-path="url(#side-clip)">
      <rect x="16" y="40" width="1168" height="460" fill="var(--wrap-white)"/>
      <polygon class="accent-band" points="924,40 1028,40 930,500 900,500" fill="var(--ink)"/>
      <polygon class="accent-field" points="1028,40 1184,40 1184,500 930,500" fill="var(--brand-orange)"/>
      <rect class="rocker-band" x="430" y="402" width="450" height="42" rx="6" fill="var(--band-dark)"/>
    </g>
    <rect class="panel-outline" x="16" y="40" width="1168" height="460" rx="26"/>

    <text class="tagline" x="542" y="92" font-size="32" textLength="356" lengthAdjust="spacingAndGlyphs">Brightway, All the Way or You'll Save <tspan class="price">$39</tspan></text>

    <rect class="mascot-area" role="img" aria-label="Illustration of two cheerful technicians in red caps and uniforms" x="500" y="108" width="200" height="292" rx="14"/>

    <text class="brand-name" x="708" y="230" font-size="40" textLength="180" lengthAdjust="spacingAndGlyphs">BRIGHTWAY</text>
    <text class="brand-name" x="708" y="262" font-size="21" textLength="172" lengthAdjust="spacingAndGlyphs">TRADESMEN</text>

    <g class="service-list">
      <rect class="service-chip" x="792" y="288" width="86" height="19" rx="3"/>
      <text class="service-label" x="873" y="303" font-size="15" text-anchor="end">HEATING</text>
      <rect class="service-chip" x="786" y="313" width="92" height="19" rx="3"/>
      <text class="service-label" x="873" y="328" font-size="15" text-anchor="end">COOLING</text>
      <rect class="service-chip" x="774" y="338" width="104" height="19" rx="3"/>
      <text class="service-label" x="873" y="353" font-size="15" text-anchor="end">PLUMBING</text>
      <rect class="service-chip" x="716" y="364" width="162" height="19" rx="3"/>
      <text class="service-label" x="873" y="379" font-size="15" text-anchor="end">DRAIN CLEANING</text>
    </g>

    <text class="web-address" x="548" y="433" font-size="28" textLength="300" lengthAdjust="spacingAndGlyphs" fill="var(--wrap-white)">GoBrightwayFix.com</text>

    <text class="phone" transform="translate(1060 270) rotate(-62)" x="0" y="14" font-size="42" text-anchor="middle" textLength="330" lengthAdjust="spacingAndGlyphs">515-555-0187</text>
  </g>

  <!-- Rear panel -->
  <g class="rear-panel">
    <g clip-path="url(#rear-clip)">
      <rect x="384" y="608" width="432" height="452" fill="var(--brand-orange)"/>
      <rect x="418" y="628" width="364" height="380" rx="10" fill="var(--wrap-white)"/>
      <rect class="phone-band" x="384" y="998" width="432" height="62" fill="var(--ink)"/>
    </g>
    <rect class="panel-outline" x="384" y="608" width="432" height="452" rx="28"/>

    <text class="tagline" x="434" y="670" font-size="27" textLength="332" lengthAdjust="spacingAndGlyphs">Brightway, All the Way or You'll Save <tspan class="price">$39</tspan></text>

    <rect class="mascot-area" role="img" aria-label="Illustration of two cheerful technicians in red caps and uniforms" x="436" y="688" width="154" height="256" rx="12"/>

    <text class="brand-name" x="596" y="782" font-size="34" textLength="170" lengthAdjust="spacingAndGlyphs">BRIGHTWAY</text>
    <text class="brand-name" x="596" y="808" font-size="19" textLength="160" lengthAdjust="spacingAndGlyphs">TRADESMEN</text>

    <g class="service-list">
      <rect class="service-chip" x="680" y="845" width="86" height="19" rx="3"/>
      <text class="service-label" x="761" y="860" font-size="15" text-anchor="end">HEATING</text>
      <rect class="service-chip" x="674" y="871" width="92" height="19" rx="3"/>
      <text class="service-label" x="761" y="886" font-size="15" text-anchor="end">COOLING</text>
      <rect class="service-chip" x="662" y="897" width="104" height="19" rx="3"/>
      <text class="service-label" x="761" y="912" font-size="15" text-anchor="end">PLUMBING</text>
      <rect class="service-chip" x="603" y="923" width="163" height="19" rx="3"/>
      <text class="service-label" x="761" y="938" font-size="15" text-anchor="end">DRAIN CLEANING</text>
    </g>

    <text class="web-address" x="566" y="988" font-size="20" textLength="198" lengthAdjust="spacingAndGlyphs" fill="var(--ink)">GoBrightwayFix.com</text>

    <text class="phone" x="600" y="1043" font-size="40" text-anchor="middle" textLength="322" lengthAdjust="spacingAndGlyphs">515-555-0187</text>
  </g>
</svg>
</body>
</html>
```